Harbor Print Studio gallery website

I need a Website for a gallery with a shopify integration or maybe even better also compatible with squarespace.
the website should have following riders: Künstler, Veranstaltungen, Shop, About Us.
some nice examples for inspiration of the website architecture are:
https://www.tarnelgalerie.com/
https://www.mossline-gallery.com/de/
https://zinnbergalerie.de/
It should be easy for us to make adaptations and fill the website with new content.
Attached there is the CI an logo for the brand.
Art Collectors,
artgallery
3 page

```html
<!DOCTYPE html>
<html lang="en">
<head>
<meta charset="utf-8">
<title>Harbor Print Studio – Gallery</title>
<link rel="stylesheet" href="https://fonts.googleapis.com/css2?family=Ubuntu:wght@300;400;500;700&display=swap">
<style>
:root{
  --red:#c4161c;
  --ink:#1b1b1b;
  --text:#3a3a3a;
  --muted:#666;
  --white:#fff;
  --stone-1:#d9d9d9;
  --stone-2:#ececec;
  --black:#000;
}
*{box-sizing:border-box;margin:0;padding:0}
html,body{width:1200px;height:3936px;overflow:hidden}
body{font-family:"Ubuntu",sans-serif;color:var(--text);background:var(--white)}
.btn{display:inline-block;font-size:13px;letter-spacing:1px;text-transform:uppercase;padding:14px 30px;text-decoration:none}
.btn-solid{background:var(--red);color:var(--white)}
.btn-outline{border:1px solid var(--red);color:var(--red);background:var(--white);padding:11px 26px;font-size:12px}
.section-title{font-weight:300;font-size:40px;color:var(--ink);text-align:center;text-transform:uppercase;letter-spacing:1px}
.stone{background:radial-gradient(ellipse at 30% 20%,#f1f1f1 0%,transparent 60%),radial-gradient(ellipse at 80% 70%,#cfcfcf 0%,transparent 55%),linear-gradient(135deg,var(--stone-2),var(--stone-1))}

/* wordmark */
.brand{display:flex;align-items:center;gap:10px;color:var(--white)}
.brand-dot{width:10px;height:10px;border-radius:50%;background:currentColor}
.brand-name{font-size:18px;font-weight:400;letter-spacing:1px;white-space:nowrap}

/* hero */
.hero{position:relative;height:672px;background:linear-gradient(180deg,#2a2a2c 0%,#3b3636 45%,#2b2727 100%);overflow:hidden}
.hero-photo{position:absolute;inset:0;background:radial-gradient(ellipse at 20% 50%,#6b5a4c 0%,transparent 45%),radial-gradient(ellipse at 85% 45%,#7a4340 0%,transparent 40%),radial-gradient(ellipse at 55% 55%,#4a4a50 0%,transparent 50%);opacity:.7}
.hero-shade{position:absolute;inset:0;background:rgba(0,0,0,.35)}
.nav{position:absolute;top:0;left:0;right:0;height:150px;display:flex;align-items:center;justify-content:space-between;padding:0 120px 0 80px;height:120px}
.menu{display:flex;gap:40px;list-style:none;align-items:center}
.menu a{color:var(--white);text-decoration:none;font-size:15px;font-weight:500;text-transform:uppercase}
.cart{position:relative;width:26px;height:22px}
.cart-badge{position:absolute;top:-8px;right:-8px;width:15px;height:15px;border-radius:50%;background:var(--red);color:#fff;font-size:10px;text-align:center;line-height:15px}
.hero-copy{position:absolute;top:256px;left:0;right:0;text-align:center;color:var(--white);font-weight:300;text-transform:uppercase}
.hero-copy .kicker{font-size:38px;letter-spacing:1px}
.hero-copy .title{font-size:64px;line-height:1.05}
.hero-copy .city{font-size:36px;letter-spacing:1px}
.hero-copy .btn{margin-top:34px}

/* about */
.about{height:528px;display:flex;align-items:center;padding:0 72px}
.about-frame{width:508px;height:408px;background:var(--black);padding:14px}
.about-mat{width:100%;height:100%;background:var(--white);padding:16px;display:flex}
.about-logo{width:170px;display:flex;align-items:center;justify-content:center;color:var(--ink)}
.about-logo .brand-name{font-size:15px;white-space:normal;text-align:center;line-height:1.3}
.about-photo{flex:1;background:linear-gradient(160deg,#d9d4cc,#b8a48a 55%,#8a7a68)}
.about-copy{margin-left:44px;width:500px}
.about-copy h2{font-weight:300;font-size:30px;color:var(--ink);text-transform:uppercase;margin-bottom:18px}
.about-copy p{font-size:14px;line-height:1.55;margin-bottom:26px}

/* shop */
.shop{height:712px;padding-top:66px}
.shop .lead{text-align:center;font-size:13px;margin-top:12px}
.shop-grid{display:flex;justify-content:space-between;padding:0 88px;margin-top:40px}
.product{width:300px;text-align:center}
.frame{background:var(--black);padding:12px}
.frame .mat{background:var(--white);padding:12px}
.product .art{height:340px}
.product .caption{font-size:14px;margin-top:26px}
.product .price{color:var(--red);font-size:15px;margin-top:4px}

/* artists */
.artists{height:720px;padding-top:64px;text-align:center}
.artists .lead{font-size:13px;line-height:1.55;width:900px;margin:14px auto 0}
.artist-grid{display:flex;justify-content:space-between;padding:0 80px;margin-top:36px}
.artist{width:192px}
.artist .frame{padding:9px}
.artist .frame .mat{padding:9px}
.artist .portrait{height:210px}
.artist h3{color:var(--red);font-size:19px;font-weight:700;margin-top:18px}
.artist p{font-size:13px;line-height:1.4;margin-top:4px}
.artists .btn{margin-top:52px}

/* events */
.events{height:748px;padding-top:72px}
.event-grid{display:flex;justify-content:space-between;padding:0 72px;margin-top:42px}
.event{width:320px;height:516px;background:var(--white);box-shadow:0 2px 10px rgba(0,0,0,.08)}
.event .pic{height:276px}
.event .body{padding:26px 26px}
.event .date{color:var(--red);font-size:13px}
.event h3{font-weight:400;font-size:22px;color:var(--ink);text-transform:uppercase;margin:10px 0}
.event p{font-size:13px;line-height:1.5;margin-bottom:20px}

/* newsletter */
.newsletter{height:340px;padding-top:68px;text-align:center}
.newsletter .section-title{font-size:38px}
.newsletter p{font-size:17px;line-height:1.5;margin:14px auto 0;width:560px}
.signup{width:632px;height:60px;margin:28px auto 0;border:1px solid #cfcfcf;display:flex;align-items:center;justify-content:space-between;padding:0 22px;font-size:14px;color:var(--muted);box-shadow:0 2px 8px rgba(0,0,0,.06)}

/* footer */
.footer{height:216px;background:var(--black);color:var(--white);position:relative;padding:0 30px}
.footer-links{position:absolute;left:30px;top:64px;display:flex;gap:10px;font-size:13px;text-transform:uppercase}
.footer-links a{color:var(--white);text-decoration:none}
.copyright{position:absolute;left:30px;top:100px;font-size:12px;color:#bbb}
.footer .brand{position:absolute;left:50%;top:100px;transform:translateX(-50%)}
.follow{position:absolute;right:30px;top:60px;text-align:center;font-size:13px;text-transform:uppercase}
.socials{display:flex;gap:12px;margin-top:18px}
.socials span{width:34px;height:34px;border-radius:50%;border:2px solid var(--red)}
</style>
</head>
<body>

<header class="hero">
  <div class="hero-photo" role="img" aria-label="Visitors viewing colourful paintings in a gallery hall"></div>
  <div class="hero-shade"></div>
  <nav class="nav">
    <div class="brand"><span class="brand-dot"></span><span class="brand-name">Harbor Print Studio</span></div>
    <ul class="menu">
      <li><a href="#">Home</a></li>
      <li><a href="#">Artists</a></li>
      <li><a href="#">Events</a></li>
      <li><a href="#">Shop</a></li>
      <li><a href="#">About Us</a></li>
      <li class="cart">
        <svg width="26" height="22" viewBox="0 0 26 22" fill="none" stroke="#fff" stroke-width="2"><path d="M1 2h4l3 12h13l3-9H7"/><circle cx="10" cy="19" r="1.6" fill="#fff"/><circle cx="19" cy="19" r="1.6" fill="#fff"/></svg>
        <span class="cart-badge">0</span>
      </li>
    </ul>
  </nav>
  <div class="hero-copy">
    <div class="kicker">Latest Collection by</div>
    <div class="title">Harbor Print Studio</div>
    <div class="city">Humburg</div>
    <a class="btn btn-solid" href="#">Buy Now</a>
  </div>
</header>

<section class="about">
  <div class="about-frame">
    <div class="about-mat">
      <div class="about-logo"><span class="brand-name">Harbor Print Studio</span></div>
      <div class="about-photo" role="img" aria-label="Gallery owner holding paintbrushes in the studio"></div>
    </div>
  </div>
  <div class="about-copy">
    <h2>About Harbor Print Studio</h2>
    <p>Our studio prints and frames limited editions for collectors. Each work is produced in close contact with the artist, checked by hand and signed before it leaves the house. We show new series every season, host open evenings and help you find the piece that fits your walls and your collection.</p>
    <a class="btn btn-solid" href="#">Read More</a>
  </div>
</section>

<section class="shop stone">
  <h2 class="section-title">Shop</h2>
  <p class="lead">Browse framed prints and originals from our current artists, available to order online and shipped ready to hang.</p>
  <div class="shop-grid">
    <div class="product">
      <div class="frame"><div class="mat"><div class="art" role="img" aria-label="Colourful painting of a harbour town at sunset" style="background:linear-gradient(160deg,#f2a65a,#d7546a 45%,#3a6fb0)"></div></div></div>
      <p class="caption">Harbor light, limited edition print</p>
      <p class="price">$25.00</p>
    </div>
    <div class="product">
      <div class="frame"><div class="mat"><div class="art" role="img" aria-label="Abstract city skyline painting in gold and black" style="background:linear-gradient(170deg,#e9c24a,#8a7a55 50%,#222)"></div></div></div>
      <p class="caption">City in gold, signed print</p>
      <p class="price">$25.00</p>
    </div>
    <div class="product">
      <div class="frame"><div class="mat"><div class="art" role="img" aria-label="Vivid painting of a close-up eye in bright colours" style="background:radial-gradient(circle at 50% 50%,#2b8fd6 0%,#e2459a 40%,#f3b33d 80%)"></div></div></div>
      <p class="caption">Colour study, framed edition</p>
      <p class="price">$25.00</p>
    </div>
  </div>
</section>

<section class="artists">
  <h2 class="section-title">Artists</h2>
  <p class="lead">Meet the painters, photographers and illustrators whose editions we print. Each one works with us from first proof to final signature, so every piece carries their hand.</p>
  <div class="artist-grid">
    <div class="artist"><div class="frame"><div class="mat"><div class="portrait" role="img" aria-label="Portrait of an artist" style="background:linear-gradient(180deg,#8a7f75,#4d4540)"></div></div></div><h3>Artist Name</h3><p>Painter working in oil and mixed media</p></div>
    <div class="artist"><div class="frame"><div class="mat"><div class="portrait" role="img" aria-label="Portrait of an artist" style="background:linear-gradient(180deg,#a08a74,#5b4a3c)"></div></div></div><h3>Artist Name</h3><p>Painter working in oil and mixed media</p></div>
    <div class="artist"><div class="frame"><div class="mat"><div class="portrait" role="img" aria-label="Portrait of an artist" style="background:linear-gradient(180deg,#c9c3bb,#7a7c82)"></div></div></div><h3>Artist Name</h3><p>Painter working in oil and mixed media</p></div>
    <div class="artist"><div class="frame"><div class="mat"><div class="portrait" role="img" aria-label="Portrait of an artist" style="background:linear-gradient(180deg,#6e8a78,#2f3b3a)"></div></div></div><h3>Artist Name</h3><p>Painter working in oil and mixed media</p></div>
    <div class="artist"><div class="frame"><div class="mat"><div class="portrait" role="img" aria-label="Portrait of an artist" style="background:linear-gradient(180deg,#d8a878,#7a5238)"></div></div></div><h3>Artist Name</h3><p>Painter working in oil and mixed media</p></div>
  </div>
  <a class="btn btn-solid" href="#">All Artists</a>
</section>

<section class="events stone">
  <h2 class="section-title">Events</h2>
  <div class="event-grid">
    <article class="event">
      <div class="pic" role="img" aria-label="Bright gallery room with paintings on white walls" style="background:linear-gradient(180deg,#e8e2d6,#a89a86)"></div>
      <div class="body"><p class="date">05, March, 2024</p><h3>Excepteur sint occaec</h3><p>Join us for the opening of a new series, with the artist present and drinks served in the gallery.</p><a class="btn btn-outline" href="#">Read More</a></div>
    </article>
    <article class="event">
      <div class="pic" role="img" aria-label="Visitors at an exhibition opening" style="background:linear-gradient(180deg,#6a5f58,#3a3230)"></div>
      <div class="body"><p class="date">05, March, 2024</p><h3>Excepteur sint occaec</h3><p>Join us for the opening of a new series, with the artist present and drinks served in the gallery.</p><a class="btn btn-outline" href="#">Read More</a></div>
    </article>
    <article class="event">
      <div class="pic" role="img" aria-label="Visitor looking at large colourful canvases" style="background:linear-gradient(160deg,#c85a4a,#3f6ea8 50%,#d9b34a)"></div>
      <div class="body"><p class="date">05, March, 2024</p><h3>Excepteur sint occaec</h3><p>Join us for the opening of a new series, with the artist present and drinks served in the gallery.</p><a class="btn btn-outline" href="#">Read More</a></div>
    </article>
  </div>
</section>

<section class="newsletter">
  <h2 class="section-title">Subscribe to our Newsletter</h2>
  <p>With our newsletter you won't miss any exhibitions. You will also receive special offers and always receive the latest news.</p>
  <div class="signup"><span>Please enter your email address</span>
    <svg width="22" height="16" viewBox="0 0 22 16" fill="none" stroke="#c4161c" stroke-width="2.4"><path d="M1 8h18M13 2l6 6-6 6"/></svg>
  </div>
</section>

<footer class="footer">
  <nav class="footer-links"><a href="#">Home</a>/<a href="#">Artists</a>/<a href="#">Events</a>/<a href="#">Shop</a>/<a href="#">About Us</a></nav>
  <p class="copyright">© 2024 Harbor Print Studio All Rights Reserved</p>
  <div class="brand"><span class="brand-dot"></span><span class="brand-name">Harbor Print Studio</span></div>
  <div class="follow">Follow us on
    <div class="socials"><span></span><span></span><span></span><span></span></div>
  </div>
</footer>

</body>
</html>
```